Flyer Design

Create a flyer using the logo theme. Single page for to be sent out on email. Attached is an image of the layout, below is the text. A5 and a4 versions.

Simplifying the MAZE

This short workshop is designed as a refresher for those surgeons who have attended a full Cox-MAZE training course, and wish to gain an update on the latest thinking with regards to the surgical treatment of Atrial Fibrillation.
We will start with an overview of the disease burden, talk to the foundation clinical evidence available, and cover the various lesion sets used by surgeons – with a view to simplifying the procedure. The workshop will also explain the technology used, how to treat the Left Atrial Appendage, the best ways to work with your EP colleagues, and involve a short hands-on session to familiarize you with the tools available to perform the Cox-MAZE procedure.

Faculty
{{image}}
Mr. Corwen Halse
Cardiothoracic Surgeon

Mr Halses training was completed at the Brannock Clinic, Rochester, Minnesota, between June 1995 and July 1997 followed by an advanced fellowship with Professor Osric J Talmane at the Westvale General Hospital. Additional expertise required visits to Belgium, Italy, England and the United States. Mr Halse now proctors internationally in order to share his knowledge and further improvement in all areas of minimal access and open cardiac and thoracic surgery.
Further overseas experience at the Westvale General Hospital in Canada culminated in the award of Clinical Fellowship in Cardiovascular Surgery in December 1997.

Mr Halse has contributed to many publications and is referee for Journal articles in very highly regarded professional journals. He performs both Cardiac surgery procedures and thoracic procedures at Harrowgate Private Hospital and Venholt Hospital, Melbourne. Mr Halse has performed in excess of 200 open Maze procedures and 35 via a Thoracoscopic approach.

Venue - TBA
Time : 5pm - 7.30pm, followed by dinner and case presentations

```html
<!DOCTYPE html>
<html lang="en">
<head>
<meta charset="utf-8">
<title>Simplifying the MAZE – Workshop Flyer</title>
<link href="https://fonts.googleapis.com/css2?family=Open+Sans:ital,wght@0,400;0,600;0,700;0,800;1,400;1,600;1,700&display=swap" rel="stylesheet">
<style>
  :root {
    --blue: #1b6fb8;
    --blue-deep: #174f93;
    --blue-light: #6fb3e6;
    --orange: #f07d19;
    --ink: #1f4e8c;
    --text: #2a2a2a;
    --white: #ffffff;
  }
  * { margin: 0; padding: 0; box-sizing: border-box; }
  html, body { width: 849px; height: 1200px; overflow: hidden; background: var(--white); }
  body { font-family: "Open Sans", Arial, sans-serif; }
  .flyer { position: relative; width: 849px; height: 1200px; overflow: hidden; background: var(--white); }
  .decor { position: absolute; left: 0; top: 0; width: 849px; height: 1200px; }

  .brand { position: absolute; left: 34px; top: 18px; }
  .brand-name { font-size: 50px; font-weight: 800; color: var(--orange); line-height: 1; letter-spacing: -0.5px; }
  .brand-region { font-size: 12px; font-weight: 700; color: var(--white); letter-spacing: 1.2px; margin-top: 6px; padding-left: 4px; }

  .quote { position: absolute; top: 166px; font-size: 130px; font-weight: 800; color: var(--orange); line-height: 1; font-family: Georgia, serif; }
  .quote-open { left: 60px; }
  .quote-close { right: 60px; }
  .title { position: absolute; top: 196px; left: 0; width: 849px; text-align: center; font-size: 50px; font-weight: 700; color: var(--ink); letter-spacing: -0.5px; }

  .intro { position: absolute; left: 90px; width: 669px; text-align: center; font-style: italic; font-size: 16px; line-height: 1.4; color: var(--ink); }
  .intro-lead { top: 276px; }
  .intro-detail { top: 370px; }

  .portrait { position: absolute; left: 60px; top: 690px; width: 190px; height: 190px; border-radius: 50%; border: 8px solid var(--orange); background: radial-gradient(circle at 50% 40%, #c9a98e 0%, #8d7462 45%, #4a5a72 100%); }
  .faculty-tag { position: absolute; left: 0; top: 900px; width: 290px; height: 116px; background: var(--blue); color: var(--white); padding: 20px 20px 0 34px; text-align: right; }
  .faculty-name { font-size: 22px; font-weight: 700; font-style: italic; line-height: 1.25; }
  .faculty-role { font-size: 20px; font-weight: 600; font-style: italic; line-height: 1.3; }

  .bio { position: absolute; left: 330px; top: 662px; width: 488px; font-size: 14.2px; line-height: 1.42; color: var(--text); }
  .bio p + p { margin-top: 14px; }

  .event { position: absolute; right: 30px; top: 1040px; text-align: right; color: var(--orange); font-weight: 700; font-size: 28px; line-height: 1.2; }
  .event-extra { position: absolute; right: 30px; top: 1164px; color: var(--white); font-weight: 700; font-size: 20px; }
</style>
</head>
<body>
<div class="flyer">
  <svg class="decor" viewBox="0 0 849 1200" aria-hidden="true">
    <path d="M0 0 H849 V120 C640 70 420 150 0 110 Z" fill="var(--blue)"/>
    <path d="M380 0 H849 V80 C700 40 560 40 380 0 Z" fill="var(--orange)"/>
    <path d="M0 110 C420 150 640 70 849 120 V140 C640 92 420 172 0 132 Z" fill="var(--blue-light)"/>
    <path d="M0 612 C260 584 560 642 849 594 V614 C560 662 260 604 0 632 Z" fill="var(--blue)"/>
    <path d="M0 632 C260 604 560 662 849 614 V626 C560 674 260 618 0 646 Z" fill="var(--orange)"/>
    <path d="M0 1016 H290 V1040 C200 1070 90 1090 0 1126 Z" fill="var(--blue-deep)"/>
    <path d="M0 1200 V1176 C260 1146 520 1162 849 1148 V1200 Z" fill="var(--blue)"/>
    <path d="M0 1176 C260 1146 520 1162 849 1148 V1156 C520 1170 260 1154 0 1184 Z" fill="var(--orange)"/>
  </svg>

  <div class="brand">
    <div class="brand-name">Valcora</div>
    <div class="brand-region">AUSTRALIA AND NEW ZEALAND</div>
  </div>

  <div class="quote quote-open">&ldquo;</div>
  <div class="quote quote-close">&rdquo;</div>
  <h1 class="title">Simplifying the MAZE</h1>

  <p class="intro intro-lead">This short workshop is designed as a refresher for those surgeons who have attended a full Cox-MAZE training course, and wish to gain an update on the latest thinking with regards to the surgical treatment of Atrial Fibrillation.</p>
  <p class="intro intro-detail">We will start with an overview of the disease burden talk to the foundation clinical evidence available and cover the various lesion sets used by surgeons – with a view to simplifying the procedure.<br><br>The workshop will also explain the technology used<br>- how to treat the Left Atrial Appendage<br>- the best ways to work with your EP colleagues<br>- involve a short hands-on session to familiarize<br>you with the tools available to perform the Cox-MAZE procedure.</p>

  <div class="portrait" role="img" aria-label="Portrait photograph of the faculty surgeon"></div>
  <div class="faculty-tag">
    <div class="faculty-name">Mr. Corwen Halse</div>
    <div class="faculty-role">Cardiothoracic Surgeon<br>Faculty</div>
  </div>

  <div class="bio">
    <p>Mr Halses training was completed at the Brannock Clinic, Rochester, Minnesota, between June 1995 and July 1997 followed by an advanced fellowship with Professor Osric J Talmane at the Westvale General Hospital. Additional expertise required visits to Belgium, Italy, England and the United States. Mr Halse now proctors internationally in order to share his knowledge and further improvement in all areas of minimal access and open cardiac and thoracic surgery.</p>
    <p>Further overseas experience at the Westvale General Hospital in Canada culminated in the award of Clinical Fellowship in Cardiovascular Surgery in December 1997.</p>
    <p>Mr Halse has contributed to many publications and is referee for Journal articles in very highly regarded professional journals. He performs both Cardiac surgery procedures and thoracic procedures at Harrowgate Private Hospital and Venholt Hospital, Melbourne. Mr Halse has performed in excess of 200 open Maze procedures and 35 via a Thoracoscopic approach.</p>
  </div>

  <div class="event">Venue - TBA<br>Time : 5pm - 7.30pm</div>
  <div class="event-extra">followed by Dinner and Case Presentations</div>
</div>
</body>
</html>
```